Business Card Design Project

Need a business card designed for a horse racing/gambling centered company.
Company name is BrightQuill.com.au
Company colours are similar to those in the logo.
Something clean and modern , designer given liberty to be creative.
Incorporate the logo is preferred.
Single or Double Sided fine
Must include :
Name
Mobile Number
Email Address
Reason: Apologies, I have been traveling unexpectedly with business and just need the extra two days to reply and give feedback before making a decision.
Industry/Entity Type
Business

```html
<!DOCTYPE html>
<html lang="en">
<head>
<meta charset="utf-8">
<title>BrightQuill.com.au – Business Card</title>
<link rel="stylesheet" href="https://fonts.googleapis.com/css2?family=Questrial&display=swap">
<style>
  :root {
    --backdrop: #c9c9c9;
    --card: #f3f4f4;
    --ink: #111111;
    --ink-soft: #2b2b2b;
    --teal: #2a8f8a;
    --teal-pale: #bcd9d7;
  }
  * { margin: 0; padding: 0; box-sizing: border-box; }
  html, body {
    width: 1200px;
    height: 682px;
    overflow: hidden;
    background: var(--backdrop);
    font-family: "Questrial", "Century Gothic", sans-serif;
  }
  .stage {
    position: relative;
    width: 1200px;
    height: 682px;
  }
  .card {
    position: absolute;
    top: 192px;
    width: 498px;
    height: 299px;
    background: var(--card);
    border-radius: 6px;
    overflow: hidden;
  }
  .card--front { left: 68px; }
  .card--back { left: 628px; }

  .holder-name {
    position: absolute;
    right: 36px;
    top: 130px;
    font-size: 50px;
    line-height: 1;
    color: var(--ink);
    font-weight: 400;
    letter-spacing: 0.5px;
  }
  .name-rule {
    position: absolute;
    left: 22px;
    top: 194px;
    width: 452px;
    height: 2px;
    background: linear-gradient(to right,
      rgba(42,143,138,0) 0%,
      var(--teal-pale) 18%,
      var(--ink-soft) 55%,
      var(--teal) 82%,
      rgba(42,143,138,0) 100%);
  }
  .contact-list {
    position: absolute;
    left: 38px;
    top: 206px;
    list-style: none;
    font-size: 15px;
    line-height: 24.5px;
    color: var(--ink-soft);
  }

  .brand-rule {
    position: absolute;
    left: 22px;
    top: 219px;
    width: 454px;
    height: 2px;
    background: linear-gradient(to right,
      rgba(42,143,138,0) 0%,
      var(--teal-pale) 20%,
      var(--teal) 50%,
      var(--teal-pale) 80%,
      rgba(42,143,138,0) 100%);
  }
  .brand {
    position: absolute;
    left: 0;
    right: 0;
    top: 128px;
    display: flex;
    align-items: center;
    justify-content: center;
    gap: 12px;
  }
  .brand-dot {
    width: 26px;
    height: 26px;
  }
  .brand-name {
    font-size: 30px;
    line-height: 1;
    color: var(--teal);
    letter-spacing: 0.5px;
  }
</style>
</head>
<body>
  <main class="stage">
    <section class="card card--front" aria-label="Card front">
      <h1 class="holder-name">John Doe</h1>
      <div class="name-rule"></div>
      <ul class="contact-list">
        <li class="contact-phone">Phone: 123-456-789</li>
        <li class="contact-email">E-mail: john@brightquill.com.au</li>
        <li class="contact-web">BrightQuill.com.au</li>
      </ul>
    </section>

    <section class="card card--back" aria-label="Card back">
      <div class="brand-rule"></div>
      <div class="brand">
        <svg class="brand-dot" viewBox="0 0 26 26" aria-hidden="true">
          <circle cx="13" cy="13" r="12" fill="var(--teal)"/>
        </svg>
        <span class="brand-name">BrightQuill.com.au</span>
      </div>
    </section>
  </main>
</body>
</html>
```